HARLOWE CONSERVATORY SAXOPHONE SENIOR RECITAL

I need a poster design for my senior saxophone recital. The title of it is "Quill: a Voyage beneath the Edge of Tone". My concept is completely contrasting to the idea of a typical university recital. I'm so put off by the idea of "clap..clap..{play some music}..clap..clap..repeat". My recital is all based off of sound. The music I selected is all very modern (i.e Brem Ostrakel 'Warm from the First Pour' for Saxophone and Coffee Machine). I've included the Chatterbox link so you can see the picture I have in the background. I like the idea of minimal black and white photography. Also, I would like the time / date / location / etc. all included on it. Let your imaginations run wild! It's art for an artist!
https://www.chatterbox-example.net/events/412093857716230/
Target Market(s)
University Students around the Harlowe Conservatory and locals around the art district of South Beach, FL.
Industry/Entity Type
University
Look and feel

```html
<!DOCTYPE html>
<html lang="en">
<head>
<meta charset="utf-8">
<title>Quill: a Voyage beneath the Edge of Tone — Recital Poster</title>
<link rel="stylesheet" href="https://fonts.googleapis.com/css2?family=Roboto+Condensed:wght@400;700&display=swap">
<style>
  :root {
    --stage: #3a3a3a;
    --poster-black: #000000;
    --ink-white: #ffffff;
    --panel-grey: #2e2e2e;
    --footer-grey: #2a2a2a;
    --label-grey: #3c3c3c;
    --photo-light: #9a9a9a;
    --photo-dark: #0c0c0c;
    --badge: #5b5b5b;
  }
  html, body {
    margin: 0;
    padding: 0;
    width: 1200px;
    height: 1000px;
    overflow: hidden;
    background: var(--stage);
  }
  .poster {
    position: absolute;
    left: 300px;
    top: 100px;
    width: 585px;
    height: 783px;
    box-shadow: 2px 3px 6px rgba(0,0,0,0.55);
  }
  .poster svg {
    display: block;
    font-family: "Roboto Condensed", "Arial Narrow", sans-serif;
  }
  .title-main { font-weight: 700; font-size: 132px; fill: var(--ink-white); }
  .title-sub { font-weight: 400; font-size: 35px; fill: var(--ink-white); }
  .title-key { font-weight: 400; font-size: 46px; fill: var(--poster-black); }
  .title-line { font-weight: 400; font-size: 46px; fill: var(--ink-white); }
  .date-month { font-weight: 400; font-size: 31px; fill: var(--ink-white); }
  .date-day { font-weight: 700; font-size: 78px; fill: var(--ink-white); }
  .date-time { font-weight: 400; font-size: 44px; fill: var(--ink-white); }
  .works-label { font-weight: 700; font-size: 10px; fill: var(--ink-white); }
  .works-item { font-weight: 400; font-size: 7.6px; fill: var(--ink-white); }
  .social-name { font-weight: 400; font-size: 12px; fill: var(--ink-white); }
  .footer-title { font-weight: 400; font-size: 11px; fill: var(--ink-white); }
  .footer-title .strong { font-weight: 700; }
  .venue { font-weight: 400; font-size: 16px; fill: var(--ink-white); }
</style>
</head>
<body>
  <div class="poster">
    <svg width="585" height="783" viewBox="0 0 585 783" xmlns="http://www.w3.org/2000/svg">
      <defs>
        <radialGradient id="portraitTone" cx="0.55" cy="0.45" r="0.6">
          <stop offset="0" stop-color="var(--photo-light)"/>
          <stop offset="0.5" stop-color="#3a3a3a"/>
          <stop offset="1" stop-color="var(--photo-dark)"/>
        </radialGradient>
        <linearGradient id="portraitSplit" x1="0" y1="0" x2="1" y2="0">
          <stop offset="0" stop-color="#000" stop-opacity="0.7"/>
          <stop offset="0.3" stop-color="#000" stop-opacity="0"/>
          <stop offset="0.45" stop-color="#000" stop-opacity="0"/>
          <stop offset="0.5" stop-color="#000" stop-opacity="0.75"/>
          <stop offset="1" stop-color="#000" stop-opacity="0.9"/>
        </linearGradient>
      </defs>

      <rect class="poster-ground" width="585" height="783" fill="var(--poster-black)"/>

      <g class="portrait" role="img" aria-label="Black and white portrait photograph, half the face painted white and half painted black">
        <rect x="245" y="230" width="340" height="470" fill="url(#portraitTone)"/>
        <rect x="245" y="230" width="340" height="470" fill="url(#portraitSplit)"/>
      </g>

      <g class="title" transform="translate(118,306) rotate(-20)">
        <text class="title-main" x="-12" y="-84">QUILL</text>
        <text class="title-sub" x="205" y="-52">A VOYAGE BENEATH</text>
        <rect class="title-band" x="254" y="-44" width="360" height="54" fill="var(--ink-white)"/>
        <text class="title-line" x="0" y="0">THE EDGE OF</text>
        <text class="title-key" x="262" y="0">TONE</text>
      </g>

      <g class="date-panel">
        <polygon points="0,385 235,325 245,505 0,555" fill="var(--panel-grey)"/>
        <polygon points="118,352 234,323 235,336 170,352" fill="var(--ink-white)"/>
        <polygon points="0,541 100,520 135,520 0,553" fill="var(--ink-white)"/>
        <text class="date-month" x="18" y="442">DECEMBER</text>
        <text class="date-month" x="172" y="470" text-anchor="end">2013</text>
        <text class="date-day" x="174" y="470">8</text>
        <line x1="25" y1="480" x2="228" y2="480" stroke="var(--ink-white)" stroke-width="2"/>
        <text class="date-time" x="150" y="527">2PM</text>
      </g>

      <g class="program">
        <rect x="50" y="557" width="137" height="13" fill="var(--label-grey)"/>
        <text class="works-label" x="53" y="567">WORKS BY</text>
        <text class="works-item" x="53" y="584">Lorenzo Vassari</text>
        <text class="works-item" x="53" y="592.5">Dr. Elliot Marwick *WORLD PREMIERE*</text>
        <text class="works-item" x="53" y="601">Brem Ostrakel</text>
        <text class="works-item" x="53" y="609.5">Dr. Miriam Caldry*WORLD PREMIERE*</text>
        <text class="works-item" x="53" y="618">Julian Fenrow</text>
        <text class="works-label" x="53" y="633" style="font-size:8px">INTERMISSION</text>
        <text class="works-item" x="53" y="641.5">Harold Tessing</text>
      </g>

      <g class="footer">
        <polygon points="0,725 585,673 585,783 0,783" fill="var(--footer-grey)"/>
        <rect class="social-badge" x="20" y="705" width="36" height="36" rx="4" fill="var(--badge)"/>
        <text class="social-name" x="62" y="727">Chatterbox</text>
        <text class="footer-title" x="22" y="759"><tspan class="strong">QUILL</tspan>: A VOYAGE BENEATH THE EDGE OF TONE</text>
        <text class="venue" x="565" y="743" text-anchor="end">ADAIR LINDQVIST RECITAL HALL</text>
        <text class="venue" x="565" y="762" text-anchor="end">PALM VERDE, FLORIDA 33180</text>
      </g>
    </svg>
  </div>
</body>
</html>
```